TeeVault - In Need of Logo/Packaging Design

I am looking for a logo and packaging design for my new company, "TeeVault". TeeVault is monthly subscription box that delivers golf equipment and accessories directly to the customer's door. The box will be a standard craft material Roll End Front Tuck mailer - the dimensions of the box are as follows:

9"x12"x3.5" (LxWxH)

I would like to see a simple and modern design that ultimately communicates innovation and creativity with the sport of golf. The box will be standard craft cardboard material therefore I would like to incorporate colors with good contrast; I am visualizing black/gray/white but am open to other options as well. If possible I would also like to incorporate the following slogan in some way:

Reliability & Convenience

I've attached a couple logos that I found online which I really like so you can get an idea of what I am looking for.

Thank you!

Target Market(s)

The upcoming young, millennial golfer.

Industry/Entity Type

Sporting Good

Logo Text

TeeVault

Requirements
Must have
• Logo/packaging design

```html
<!DOCTYPE html>
<html lang="en">
<head>
<meta charset="UTF-8">
<title>TeeVault Mailer Box Dieline</title>
<link rel="stylesheet" href="https://fonts.googleapis.com/css2?family=Montserrat:wght@400;500;700&display=swap">
<style>
  :root {
    --board: #323845;
    --fold: #454c5b;
    --ink: #ffffff;
    --dim: #9a9ea6;
    --dim-text: #2b2b2b;
    --page: #ffffff;
  }
  html, body {
    margin: 0;
    padding: 0;
    width: 900px;
    height: 1200px;
    overflow: hidden;
    background: var(--page);
  }
  .dieline {
    display: block;
    width: 900px;
    height: 1200px;
  }
  .panel { fill: var(--board); }
  .fold-line { stroke: var(--fold); stroke-width: 1; fill: none; }
  .slot { fill: var(--ink); }
  .brand-name {
    font-family: 'Montserrat', sans-serif;
    font-weight: 500;
    fill: var(--ink);
    letter-spacing: 0.06em;
    text-anchor: middle;
  }
  .slogan {
    font-family: 'Montserrat', sans-serif;
    font-weight: 700;
    fill: var(--ink);
    letter-spacing: 0.08em;
    text-anchor: middle;
    text-transform: uppercase;
  }
  .dim-line { stroke: var(--dim); stroke-width: 1; fill: none; }
  .dim-guide { stroke: #d4d6da; stroke-width: 1; }
  .dim-label {
    font-family: 'Montserrat', sans-serif;
    font-weight: 400;
    font-size: 17px;
    fill: var(--dim-text);
    text-anchor: middle;
  }
</style>
</head>
<body>
<svg class="dieline" viewBox="0 0 900 1200" xmlns="http://www.w3.org/2000/svg">
  <defs>
    <marker id="arrow" viewBox="0 0 10 10" refX="9" refY="5" markerWidth="6" markerHeight="6" orient="auto-start-reverse">
      <path d="M0,1 L10,5 L0,9 z" fill="#6d7178"/>
    </marker>
  </defs>

  <!-- Dimension guides -->
  <g class="dimensions">
    <line class="dim-guide" x1="308" y1="110" x2="308" y2="160"/>
    <line class="dim-guide" x1="668" y1="110" x2="668" y2="160"/>
    <line class="dim-line" x1="312" y1="122" x2="448" y2="122" marker-start="url(#arrow)"/>
    <line class="dim-line" x1="528" y1="122" x2="664" y2="122" marker-end="url(#arrow)"/>
    <text class="dim-label" x="493" y="130">12″</text>

    <line class="dim-guide" x1="30" y1="278" x2="86" y2="278"/>
    <line class="dim-guide" x1="30" y1="546" x2="86" y2="546"/>
    <line class="dim-guide" x1="30" y1="650" x2="86" y2="650"/>
    <line class="dim-line" x1="46" y1="282" x2="46" y2="385" marker-start="url(#arrow)"/>
    <line class="dim-line" x1="46" y1="440" x2="46" y2="542" marker-end="url(#arrow)"/>
    <text class="dim-label" transform="translate(52 412) rotate(90)">9″</text>
    <line class="dim-line" x1="46" y1="550" x2="46" y2="572" marker-start="url(#arrow)"/>
    <line class="dim-line" x1="46" y1="626" x2="46" y2="646" marker-end="url(#arrow)"/>
    <text class="dim-label" transform="translate(52 598) rotate(90)">3.5″</text>

    <line class="dim-guide" x1="170" y1="922" x2="226" y2="922"/>
    <line class="dim-guide" x1="170" y1="1032" x2="226" y2="1032"/>
    <line class="dim-line" x1="188" y1="926" x2="188" y2="948" marker-start="url(#arrow)"/>
    <line class="dim-line" x1="188" y1="1004" x2="188" y2="1028" marker-end="url(#arrow)"/>
    <text class="dim-label" transform="translate(194 976) rotate(90)">3.5″</text>

    <line class="dim-guide" x1="308" y1="1040" x2="308" y2="1104"/>
    <line class="dim-guide" x1="668" y1="1040" x2="668" y2="1104"/>
    <line class="dim-line" x1="312" y1="1070" x2="448" y2="1070" marker-start="url(#arrow)"/>
    <line class="dim-line" x1="528" y1="1070" x2="664" y2="1070" marker-end="url(#arrow)"/>
    <text class="dim-label" x="493" y="1078">12″</text>
  </g>

  <!-- Box panels -->
  <g class="box">
    <!-- top row: back wall with dust flaps -->
    <polygon class="panel" points="146,172 308,172 308,278 200,278 192,270 146,270"/>
    <rect class="panel" x="308" y="172" width="360" height="106"/>
    <polygon class="panel" points="668,172 832,172 832,270 784,270 776,278 668,278"/>

    <!-- middle row: base with side walls and locking flaps -->
    <polygon class="panel" points="200,278 106,278 106,330 92,336 92,384 106,388 106,436 92,442 92,490 106,494 106,546 200,546"/>
    <rect class="panel" x="200" y="278" width="108" height="268"/>
    <rect class="panel" x="308" y="278" width="360" height="268"/>
    <rect class="panel" x="668" y="278" width="108" height="268"/>
    <polygon class="panel" points="776,278 870,278 870,330 884,336 884,384 870,388 870,436 884,442 884,490 870,494 870,546 776,546"/>

    <!-- front wall row -->
    <polygon class="panel" points="146,554 192,554 200,546 776,546 784,554 832,554 832,650 146,650"/>

    <!-- lid -->
    <rect class="panel" x="308" y="650" width="360" height="272"/>

    <!-- tuck flap -->
    <path class="panel" d="M238,922 H738 V1018 Q738,1032 724,1032 H252 Q238,1032 238,1018 Z"/>

    <!-- fold lines -->
    <g>
      <line class="fold-line" x1="308" y1="172" x2="308" y2="922"/>
      <line class="fold-line" x1="668" y1="172" x2="668" y2="922"/>
      <line class="fold-line" x1="146" y1="278" x2="832" y2="278"/>
      <line class="fold-line" x1="106" y1="546" x2="870" y2="546"/>
      <line class="fold-line" x1="200" y1="278" x2="200" y2="546"/>
      <line class="fold-line" x1="776" y1="278" x2="776" y2="546"/>
      <line class="fold-line" x1="308" y1="650" x2="668" y2="650"/>
      <line class="fold-line" x1="238" y1="922" x2="738" y2="922"/>
    </g>

    <!-- locking slots -->
    <rect class="slot" x="308" y="330" width="6" height="24"/>
    <rect class="slot" x="308" y="436" width="6" height="28"/>
    <rect class="slot" x="662" y="330" width="6" height="24"/>
    <rect class="slot" x="662" y="436" width="6" height="28"/>
  </g>

  <!-- Branding -->
  <g class="branding">
    <text class="brand-name" x="488" y="240" font-size="40">TeeVault</text>

    <g transform="translate(248 412) rotate(-90)">
      <text class="brand-name" x="0" y="0" font-size="34">TeeVault</text>
      <text class="slogan" x="0" y="20" font-size="8.5">Reliability &amp; Convenience</text>
    </g>

    <g transform="translate(726 412) rotate(90)">
      <text class="brand-name" x="0" y="0" font-size="34">TeeVault</text>
      <text class="slogan" x="0" y="20" font-size="8.5">Reliability &amp; Convenience</text>
    </g>

    <g transform="translate(488 412) rotate(180)">
      <text class="brand-name" x="0" y="0" font-size="15">TeeVault</text>
      <text class="slogan" x="0" y="11" font-size="4.5">Reliability &amp; Convenience</text>
    </g>

    <g transform="translate(488 584) rotate(180)">
      <text class="brand-name" x="0" y="0" font-size="38">TeeVault</text>
    </g>

    <text class="brand-name" x="488" y="806" font-size="56">TeeVault</text>

    <text class="brand-name" x="488" y="992" font-size="40">TeeVault</text>
  </g>
</svg>
</body>
</html>
```